my personal cards just intrducing my self

Massage Therapy to get my name out their

Target Market(s)

40 year olds who enjoy massage

Industry/Entity Type

Massage

Contact Information for Business Card

Leonard T Vasquelle
LMT-Licensed Massage Therapist
*Swedish *Deep Tissue *Prenatal
*Reflexology *Chair and more

(602)-347-2916
leonardvasquelle@mailorbit.net

Font styles to use
Serif

Colors
0456a4
6b449b

```html
<!DOCTYPE html>
<html lang="en">
<head>
<meta charset="utf-8">
<title>Leonard T Vasquelle – Business Cards</title>
<link rel="stylesheet" href="https://fonts.googleapis.com/css2?family=Libre+Baskerville:wght@400&display=swap">
<style>
  :root {
    --blue: #0456a4;
    --purple: #6b449b;
    --paper: #ffffff;
    --backdrop: #a9a9a9;
    --faint: #ececec;
    --serif: "Libre Baskerville", Georgia, serif;
  }
  * { box-sizing: border-box; margin: 0; padding: 0; }
  html, body { width: 1200px; height: 900px; overflow: hidden; }
  body {
    background: var(--backdrop);
    font-family: var(--serif);
    position: relative;
  }
  .card {
    position: absolute;
    top: 290px;
    width: 540px;
    height: 316px;
    background: var(--paper);
    border-radius: 26px;
    overflow: hidden;
    box-shadow: 0 10px 24px rgba(0,0,0,0.18);
  }
  .card--front { left: 40px; }
  .card--back  { left: 620px; }

  .brand {
    position: absolute;
    left: 0; right: 0;
    display: flex;
    align-items: center;
    justify-content: center;
    gap: 10px;
    color: var(--purple);
    font-size: 17px;
  }
  .brand__dot {
    width: 16px; height: 16px;
    border-radius: 50%;
    background: var(--purple);
  }
  .identity {
    position: absolute;
    left: 0; right: 0;
    text-align: center;
    color: var(--blue);
  }
  .identity__name {
    display: inline-block;
    font-size: 22px;
    padding: 0 4px 4px;
    border-bottom: 2px solid var(--purple);
  }
  .identity__title {
    font-size: 11.5px;
    letter-spacing: 1.4px;
    margin-top: 4px;
  }

  .card--front .brand { top: 62px; }
  .card--front .identity { top: 118px; }

  .services {
    position: absolute;
    left: 0; right: 0;
    top: 186px;
    height: 22px;
    background: var(--purple);
    display: flex;
    justify-content: space-around;
    align-items: center;
    color: var(--paper);
    font-size: 12.5px;
    padding: 0 10px;
  }
  .contact {
    position: absolute;
    left: 0; right: 0;
    top: 234px;
    text-align: center;
    color: var(--blue);
    font-size: 16px;
    line-height: 1.45;
  }

  .card--back .backdrop-mark {
    position: absolute;
    right: -70px;
    top: 10px;
    width: 300px;
    height: 300px;
    border-radius: 50%;
    background: var(--faint);
  }
  .card--back .brand { top: 96px; }
  .card--back .identity { top: 160px; }
</style>
</head>
<body>
  <section class="card card--front">
    <div class="brand"><span class="brand__dot"></span><span>Vasquelle Massage</span></div>
    <div class="identity">
      <div class="identity__name">Leonard T Vasquelle</div>
      <div class="identity__title">LMT-Licensed Massage Therapist</div>
    </div>
    <div class="services">
      <span>Swedish</span><span>Deep Tissue</span><span>Prenatal</span><span>Reflexology</span><span>Chair and more</span>
    </div>
    <div class="contact">
      <div>(602)-347-2916</div>
      <div>leonardvasquelle@mailorbit.net</div>
    </div>
  </section>

  <section class="card card--back">
    <div class="backdrop-mark" aria-hidden="true"></div>
    <div class="brand"><span class="brand__dot"></span><span>Vasquelle Massage</span></div>
    <div class="identity">
      <div class="identity__name">Leonard T Vasquelle</div>
      <div class="identity__title">LMT-Licensed Massage Therapist</div>
    </div>
  </section>
</body>
</html>
```